Wine label for family vineyard start-up

Brand new family vineyard needs a new label:

The information we need on the label is the following:
- Rovere & Pietra (variety)
- Borgo Valsereno (location)
- 2018 (vintage)

The style of the label should be graphic / minimal / masculine.

This is a wine made by three 35yr old guys

Target Market(s)

young & urban

Industry/Entity Type

Vineyard

Logo Text

Rovere & Pietra / Borgo Valsereno / 2018

Font styles to use
Sans Serif

Requirements
Must have
• clearly legible
• aesthetically pleasing [minimalist]
• sans serif

```html
<!DOCTYPE html>
<html lang="en">
<head>
<meta charset="utf-8">
<title>Rovere &amp; Pietra — Borgo Valsereno 2018</title>
<link rel="stylesheet" href="https://fonts.googleapis.com/css2?family=Josefin+Sans:wght@300&display=swap">
<style>
  :root {
    --canvas-bg: #ffffff;
    --canvas-edge: #2a2a2a;
    --label-bg: #000000;
    --label-ink: #ffffff;
  }
  * { margin: 0; padding: 0; box-sizing: border-box; }
  html, body {
    width: 1200px;
    height: 1000px;
    overflow: hidden;
    background: var(--canvas-bg);
  }
  .canvas {
    position: relative;
    width: 1200px;
    height: 1000px;
    border: 1px solid var(--canvas-edge);
    background: var(--canvas-bg);
  }
  .wine-label {
    position: absolute;
    left: 406px;
    top: 209px;
    width: 388px;
    height: 582px;
    background: var(--label-bg);
    font-family: 'Josefin Sans', sans-serif;
    font-weight: 300;
    color: var(--label-ink);
    line-height: 1;
    white-space: nowrap;
  }
  .variety {
    position: absolute;
    left: 0;
    top: 346px;
    width: 388px;
    text-align: center;
    font-size: 52px;
  }
  .location {
    position: absolute;
    left: 14px;
    top: 488px;
    width: 374px;
    text-align: center;
    font-size: 31px;
    letter-spacing: 2px;
  }
  .vintage {
    position: absolute;
    left: 0;
    top: 535px;
    width: 388px;
    text-align: center;
    font-size: 30px;
    letter-spacing: 1px;
  }
</style>
</head>
<body>
  <main class="canvas">
    <section class="wine-label">
      <h1 class="variety" style="font-weight:300">Rovere&amp;Pietra</h1>
      <p class="location">Borgo Valsereno</p>
      <p class="vintage">2018</p>
    </section>
  </main>
</body>
</html>
```